Pop Up Banner Design (30x72in) for events for Meridian Tongue Institute

30 x 72 inch design for a pop up banner or 2 (or 3) to advertise my business, Meridian Tongue Institute, featuring www.meridiantongueinst.com

This banner will be used at anime conventions, or local events to promote the business to the general public, schools, or asian culture lovers.

Color scheme to identify with the logo that is attached. Imagery would be great!

Target audience: teens to 30s
Benefits MTI Offers: learning japanese language, learning japanese culture, peer study groups and events, one-on-one or classroom setting, in person or virtual learning, Standard Lexical Aptitude Exam (SLAE) preparation, homework, guided tours to Japan once a year, translation services, conversation tables, etc.

Target Market(s)

teens to 30 year olds

Industry/Entity Type

Education

Font styles to use
Sans Serif

Colors
ec1f27
ffffff
000000

Requirements
Must have
• logo, imagery, benefits strategically explained, website

```html
<!DOCTYPE html>
<html lang="en">
<head>
<meta charset="utf-8">
<title>Meridian Tongue Institute – Pop Up Banner</title>
<link rel="stylesheet" href="https://fonts.googleapis.com/css2?family=Open+Sans:wght@600;700;800&display=swap">
<style>
  :root {
    --brand-red: #ec1f27;
    --brand-red-soft: rgba(236, 31, 39, 0.18);
    --ink: #111111;
    --ink-soft: #3a3a3a;
    --paper: #ffffff;
    --paper-tint: #f1f1f1;
    --sky-top: #8fb4d8;
    --sky-low: #dfe6ee;
    --foliage: #b5432f;
    --foliage-deep: #6e3a2a;
  }
  * { margin: 0; padding: 0; box-sizing: border-box; }
  html, body {
    width: 1200px; height: 2863px; overflow: hidden;
    background: var(--paper);
  }
  .banner {
    position: relative;
    width: 1200px; height: 2863px; overflow: hidden;
    font-family: "Open Sans", Arial, sans-serif;
    background: radial-gradient(circle at 50% 45%, var(--paper) 0%, var(--paper-tint) 100%);
    color: var(--ink);
  }
  .hero {
    position: absolute; left: 0; top: 0;
    width: 1200px; height: 900px;
  }
  .brand {
    position: absolute; left: 205px; top: 84px; width: 510px;
    display: flex; flex-direction: column; align-items: center;
  }
  .brand-dot {
    width: 310px; height: 310px; border-radius: 50%;
    background: var(--brand-red);
  }
  .brand-name {
    margin-top: 22px;
    font-size: 33px; font-weight: 600; letter-spacing: 0.5px;
    color: var(--ink-soft); text-transform: uppercase; white-space: nowrap;
  }
  .headline {
    position: absolute; left: 0; top: 931px; width: 1200px;
    text-align: center;
  }
  .headline-main {
    font-size: 87px; font-weight: 800; line-height: 1.2; color: var(--ink);
  }
  .headline-sub {
    margin-top: 6px;
    font-size: 62px; font-weight: 700; line-height: 1.2; color: var(--ink);
  }
  .benefits-title {
    margin-top: 40px;
    font-size: 63px; font-weight: 800; line-height: 1.2; color: var(--brand-red);
  }
  .benefits {
    position: absolute; left: 0; top: 1282px; width: 1200px;
    list-style: none;
  }
  .benefits li {
    position: relative; padding-left: 181px; padding-right: 40px;
    font-size: 53px; font-weight: 700; line-height: 60px;
    margin-bottom: 34px; color: var(--ink);
    text-shadow: 0 2px 3px rgba(0,0,0,0.15);
  }
  .benefits li::before {
    content: ""; position: absolute; left: 118px; top: 21px;
    width: 18px; height: 18px; border-radius: 50%;
    background: var(--brand-red);
  }
  .scenery {
    position: absolute; left: 0; top: 2090px;
    width: 1200px; height: 623px;
    background:
      radial-gradient(ellipse 60% 70% at 30% 100%, var(--brand-red) 0%, rgba(236,31,39,0.75) 45%, rgba(236,31,39,0) 75%),
      radial-gradient(ellipse 45% 55% at 82% 100%, var(--brand-red) 0%, rgba(236,31,39,0.7) 45%, rgba(236,31,39,0) 75%),
      linear-gradient(180deg, rgba(236,31,39,0) 0%, var(--brand-red-soft) 60%, rgba(236,31,39,0.45) 100%);
  }
  .footer {
    position: absolute; left: 0; bottom: 0;
    width: 1200px; height: 150px;
    background: var(--brand-red);
    display: flex; align-items: center;
    padding-left: 88px;
  }
  .footer-url {
    font-size: 57px; font-weight: 700; color: var(--paper);
    letter-spacing: 0.5px; white-space: nowrap;
  }
</style>
</head>
<body>
<div class="banner">

  <svg class="hero" viewBox="0 0 1200 900" xmlns="http://www.w3.org/2000/svg">
    <defs>
      <linearGradient id="heroTones" x1="0" y1="0" x2="0" y2="1">
        <stop offset="0" stop-color="#8fb4d8"/>
        <stop offset="0.4" stop-color="#dfe6ee"/>
        <stop offset="0.7" stop-color="#b5432f"/>
        <stop offset="1" stop-color="#6e3a2a"/>
      </linearGradient>
    </defs>
    <path role="img" aria-label="Photograph of a red five-storey pagoda among autumn maple trees with a snowy mountain and city behind"
          d="M0 0 H1200 V560 Q1060 760 760 790 Q380 800 0 560 Z" fill="url(#heroTones)"/>
    <path class="brush-sweep" d="M40 820 Q500 800 860 730 Q1060 680 1200 570 L1200 610 Q1060 720 860 770 Q500 840 60 850 Z"
          fill="var(--brand-red)"/>
    <path class="brush-tail" d="M0 800 Q160 790 300 810 Q160 805 0 830 Z" fill="var(--brand-red)"/>
  </svg>

  <div class="brand">
    <div class="brand-dot"></div>
    <div class="brand-name">Meridian Tongue Institute</div>
  </div>

  <header class="headline">
    <h1 class="headline-main">Discover Japan</h1>
    <p class="headline-sub">Through Language &amp; Culture</p>
    <h2 class="benefits-title">MTI Can Help You:</h2>
  </header>

  <ul class="benefits">
    <li>Learn Japanese</li>
    <li>Virtually or In Person*</li>
    <li>One on One or Classroom setting</li>
    <li>Experience Japanese Culture</li>
    <li>Prep for the SLAE</li>
    <li>Connect with other learners</li>
    <li>One on one homework correction</li>
    <li>Practice speaking with virtual conversation tables and more!</li>
  </ul>

  <div class="scenery" role="img" aria-label="Red silhouette illustration of a pagoda, a rising sun and a bonsai tree"></div>

  <footer class="footer">
    <span class="footer-url">www.meridiantongueinst.com</span>
  </footer>

</div>
</body>
</html>
```